Road Sign at our office 84 in X 48 in - Small Billboard

Kestrel Electrical
Electrical & Lighting Services

- we need a sign design for our small business/company based in Calhoun, GA called Kestrel Electrical - "our mission is to provide Northwest Georgia with dependable, high-quality electrical services that prioritize safety, integrity, and long-term reliability. As a woman-owned business with over 25 years of experience, we are committed to delivering exceptional workmanship and personalized service for every commercial, residential, and industrial project we undertake. We stand behind our work with a lifetime warranty—because your trust is our most powerful connection."

display logo, phone number, and open to other ideas without being cluttered, maybe instead of full website address, just use @ksrelectrical and it will send them to all of our website and socials...

it needs to be easy to read as they drive down the road
this is a place where people may be traveling at high speeds, make sure it's easy to see and understand at a glance.
It will be hanging 20-24ft from the ground. Like a small billboard.

https://ksrelectricworks.com/

Industry/Entity Type

Electrical Contractor

Requirements
Nice to have
• match the look and feel of website and socials

```html
<!DOCTYPE html>
<html lang="en">
<head>
<meta charset="utf-8">
<title>Kestrel Electrical – Road Sign</title>
<link href="https://fonts.googleapis.com/css2?family=Bebas+Neue&family=Montserrat:wght@600&display=swap" rel="stylesheet">
<style>
  :root {
    --page: #ececec;
    --night: #000000;
    --flame: #e8501d;
    --amber: #f3930a;
    --white: #ffffff;
  }
  * { margin: 0; padding: 0; box-sizing: border-box; }
  html, body {
    width: 1200px;
    height: 1157px;
    overflow: hidden;
    background: var(--page);
  }
  .sign {
    position: absolute;
    left: 0;
    top: 321px;
    width: 1200px;
    height: 514px;
    background: var(--night);
    overflow: hidden;
  }
  .sign-wave {
    position: absolute;
    inset: 0;
    width: 1200px;
    height: 514px;
  }
  .brand {
    position: absolute;
    left: 66px;
    top: 104px;
    display: flex;
    align-items: center;
    gap: 34px;
  }
  .brand-dot {
    width: 132px;
    height: 132px;
    border-radius: 50%;
    background: var(--amber);
    flex: none;
  }
  .brand-name {
    font-family: "Montserrat", sans-serif;
    font-weight: 600;
    color: var(--white);
    line-height: 1;
  }
  .brand-name .word {
    display: block;
    font-size: 112px;
    letter-spacing: -1px;
  }
  .brand-name .trade {
    display: block;
    margin-top: 14px;
    font-size: 40px;
    letter-spacing: 27px;
  }
  .contact {
    position: absolute;
    left: 70px;
    right: 60px;
    top: 397px;
    font-family: "Bebas Neue", sans-serif;
    font-size: 92px;
    line-height: 1;
    color: var(--white);
    letter-spacing: 2px;
    white-space: nowrap;
  }
  .contact .divider { margin: 0 26px; }
</style>
</head>
<body>
  <section class="sign" aria-label="Kestrel Electrical road sign">
    <svg class="sign-wave" viewBox="0 0 1200 514" aria-hidden="true">
      <path d="M0 432 C120 370 230 348 420 340 C640 332 820 300 990 200 C1100 134 1160 60 1176 0 L1200 0 L1200 514 L0 514 Z" fill="var(--amber)"/>
      <path d="M0 448 C120 386 230 362 420 354 C660 346 850 312 1020 200 C1120 134 1180 60 1194 0 L1200 0 L1200 514 L0 514 Z" fill="var(--flame)"/>
    </svg>

    <div class="brand">
      <span class="brand-dot"></span>
      <h1 class="brand-name">
        <span class="word">Kestrel</span>
        <span class="trade">ELECTRICAL</span>
      </h1>
    </div>

    <p class="contact">706-555-0148<span class="divider">|</span>@KSRELECTRICAL</p>
  </section>
</body>
</html>
```